WebDesign Flyer - A5 Double Sided

We create a complete web presence for local businesses.
A comprehensive background on our services and company can be found at www.brightnetstall.co.uk and on the attached sales document.

We want these flyers (a5, double sided, colour) to portray us as a local, professional and friendly service that will take care fully of a business's online presence. This includes website, hosting, email, domain AND IMPORTANTLY: we also can build them a business profile on business directory websites such as PinTown, OurCornerHub, Vistamap Spots, Quib etc. which helps them increase their profit.

Target Market(s)

Small to medium businesses found on the high street. eg: restaurants, physios, doctors, retail shops, salons, hairdressers, as well as more corporate businesses like accountancy firms and lawyers.

Industry/Entity Type

Business Directory

Requirements
Must have
• Full project files provided with all required elements if design is chosen. Design to mention: sites can be updated in less than 1 minute in 3 clicks, No contracts, money back guarantee (no risk), prices from £400, SEO as standard, brightnetstall.co.uk, 020 7946 0381, info@brightnetstall.co.uk, 10% discount with this flyer until December 20th 2010.
Nice to have
• To mention: dedicated support, business photos (see brightnetstall.co.uk/features), Chatterly, Peepline, ReelBox, Snapvault, CareerMesh Integration, free consultation, logos of services we provide (see logos.zip for examples).
Should not have
• our logo featured too prominently.

```html
<!DOCTYPE html>
<html lang="en">
<head>
<meta charset="utf-8">
<title>Bright Net Stall – A5 Flyer, Front and Back</title>
<link href="https://fonts.googleapis.com/css2?family=Alfa+Slab+One&family=Arvo:wght@700&display=swap" rel="stylesheet">
<style>
  :root{
    --ink:#0c3767;
    --blue-deep:#15528f;
    --blue:#2f7fc4;
    --blue-light:#58a6e2;
    --yellow:#f6e630;
    --yellow-soft:#fbf08a;
    --cream:#fdfbe6;
    --white:#ffffff;
    --page:#ffffff;
  }
  *{margin:0;padding:0;box-sizing:border-box}
  html,body{width:1200px;height:943px;overflow:hidden;background:var(--page)}
  .canvas{position:relative;width:1200px;height:943px}
  .flyer{position:absolute;width:501px;height:709px;overflow:hidden;background:var(--white);
    box-shadow:6px 8px 10px rgba(0,0,0,.35)}
  .flyer--front{left:40px;top:37px}
  .flyer--back{left:604px;top:103px}
  .flyer__bg{position:absolute;inset:0}
  .t{position:absolute;white-space:nowrap;line-height:1}
  .headline{font-family:"Alfa Slab One",serif;font-size:31px;letter-spacing:.5px;
    text-shadow:2px 3px 0 var(--ink),-1px -1px 0 var(--ink),1px -1px 0 var(--ink),-1px 1px 0 var(--ink)}
  .headline--white{color:var(--white)}
  .headline--yellow{color:var(--yellow)}
  .headline--more{color:var(--blue-light);font-size:37px;
    text-shadow:2px 3px 0 var(--ink),-1px -1px 0 var(--ink),1px -1px 0 var(--ink),-1px 1px 0 var(--ink)}
  .photo{position:absolute;border-radius:50%}
  .bullet{font-family:"Arvo",serif;font-weight:700;font-size:17px;color:var(--white)}
  .arrow{position:absolute;width:0;height:0;border-top:11px solid transparent;border-bottom:11px solid transparent;border-left:24px solid var(--yellow)}
  .pounds{font-family:"Alfa Slab One",serif;color:var(--white);text-shadow:2px 2px 0 var(--ink)}
  .offer{position:absolute;left:18px;top:470px;transform:rotate(-22deg);transform-origin:left top;
    font-family:"Alfa Slab One",serif;color:var(--blue-deep);text-align:center;line-height:1}
  .offer__big{font-size:34px;display:block}
  .offer__small{font-size:17px;display:block;margin-top:2px}
  .contact{font-family:"Arvo",serif;font-weight:700;font-size:14px}
  .contact--phone{color:var(--ink)}
  .contact--email{color:var(--blue-light)}
  .brand{position:absolute;display:flex;align-items:center;gap:8px}
  .brand__mark{width:30px;height:30px;border-radius:50%;background:var(--blue-light)}
  .brand__name{font-family:"Arvo",serif;font-weight:700;font-size:22px;color:var(--blue)}
</style>
</head>
<body>
<div class="canvas">

  <!-- Front side -->
  <section class="flyer flyer--front">
    <svg class="flyer__bg" width="501" height="709" viewBox="0 0 501 709">
      <defs>
        <linearGradient id="frontBlue" x1="0" y1="0" x2="0" y2="1">
          <stop offset="0" stop-color="#1f6cb3"/><stop offset="1" stop-color="#13497f"/>
        </linearGradient>
        <linearGradient id="frontCream" x1="0" y1="0" x2="1" y2="0">
          <stop offset="0" stop-color="#fffef4"/><stop offset="1" stop-color="#f8ee9c"/>
        </linearGradient>
      </defs>
      <rect width="501" height="709" fill="#fff"/>
      <path d="M0,0H501V230H0Z" fill="var(--yellow)"/>
      <path d="M0,50 C120,15 240,110 350,70 C420,45 470,40 501,50 V440 H0Z" fill="var(--blue-light)"/>
      <path d="M0,72 C110,40 230,128 340,95 C410,74 460,66 501,78 V520 C430,560 320,430 170,428 C100,427 40,430 0,430Z" fill="url(#frontBlue)"/>
      <path d="M0,430 C40,430 100,427 170,428 C320,430 430,560 501,520 V600 C420,610 330,520 180,490 C100,470 40,470 0,470Z" fill="var(--yellow)"/>
      <path d="M0,470 C40,470 100,470 180,490 C330,520 420,610 501,600 V709 H0Z" fill="url(#frontCream)"/>
      <path d="M250,520 C330,540 420,600 501,592 V610 C420,618 330,560 250,520Z" fill="var(--blue-light)"/>
      <g fill="none" stroke="var(--blue-light)" stroke-width="3">
        <circle cx="373" cy="100" r="72"/><circle cx="373" cy="100" r="79"/><circle cx="373" cy="100" r="86"/>
        <circle cx="100" cy="247" r="56"/><circle cx="100" cy="247" r="63"/><circle cx="100" cy="247" r="70"/>
        <circle cx="398" cy="578" r="68"/><circle cx="398" cy="578" r="75"/><circle cx="398" cy="578" r="82"/>
      </g>
    </svg>

    <div class="photo" role="img" aria-label="Photo of a smiling team working together at a laptop" style="left:308px;top:35px;width:130px;height:130px;background:radial-gradient(circle at 40% 40%,#e9e6e2,#9aa6b4)"></div>
    <div class="photo" role="img" aria-label="Photo of a magnifying glass over a search engine page on a screen" style="left:52px;top:199px;width:96px;height:96px;background:radial-gradient(circle at 45% 50%,#eef3f8,#8fb0cf)"></div>
    <div class="photo" role="img" aria-label="Photo of two young professionals at a computer, one on a headset" style="left:337px;top:517px;width:122px;height:122px;background:radial-gradient(circle at 45% 45%,#f1eee9,#a9b2bc)"></div>

    <div class="t headline headline--white" style="left:35px;top:77px">BESPOKE</div>
    <div class="t headline headline--white" style="left:95px;top:113px">WEBSITE</div>
    <div class="t headline headline--yellow" style="left:205px;top:208px">S.E.O</div>
    <div class="t headline headline--white" style="left:185px;top:290px">SOCIAL MEDIA</div>
    <div class="t headline headline--yellow" style="left:123px;top:368px">BUSINESS</div>
    <div class="t headline headline--yellow" style="left:223px;top:406px">LISTINGS</div>
    <div class="t headline headline--more" style="left:52px;top:497px">and</div>
    <div class="t headline headline--more" style="left:25px;top:541px">LOTS MORE!</div>

    <div class="brand" style="left:25px;top:638px">
      <span class="brand__mark"></span><span class="brand__name">Bright Net Stall</span>
    </div>
  </section>

  <!-- Back side -->
  <section class="flyer flyer--back">
    <svg class="flyer__bg" width="501" height="709" viewBox="0 0 501 709">
      <defs>
        <linearGradient id="backBlue" x1="0" y1="0" x2="0" y2="1">
          <stop offset="0" stop-color="#13497f"/><stop offset="1" stop-color="#1f6cb3"/>
        </linearGradient>
        <linearGradient id="backYellow" x1="0" y1="0" x2="1" y2="1">
          <stop offset="0" stop-color="var(--yellow)"/><stop offset=".55" stop-color="#f9ef8c"/><stop offset="1" stop-color="#fffef6"/>
        </linearGradient>
      </defs>
      <rect width="501" height="709" fill="url(#backYellow)"/>
      <path d="M0,0H501V470 C400,480 330,420 200,395 C120,380 50,372 0,378Z" fill="var(--blue-light)"/>
      <path d="M0,0H501V420 C420,445 330,400 210,372 C130,355 50,360 0,368Z" fill="url(#backBlue)"/>
      <g fill="none" stroke="var(--white)" stroke-width="3" opacity=".9">
        <circle cx="114" cy="537" r="40"/><circle cx="114" cy="537" r="52"/><circle cx="114" cy="537" r="64"/><circle cx="114" cy="537" r="76"/>
      </g>
      <g>
        <circle cx="303" cy="52" r="18" fill="var(--yellow)"/><circle cx="303" cy="52" r="13" fill="#fff" stroke="var(--blue)" stroke-width="2"/>
        <path d="M303,44V52H309" stroke="var(--blue-deep)" stroke-width="2" fill="none"/>
      </g>
      <g>
        <circle cx="361" cy="161" r="17" fill="#fff" stroke="var(--blue-light)" stroke-width="2"/>
        <path d="M352,166L366,152M356,170L370,156M354,158H366" stroke="var(--blue)" stroke-width="2"/>
      </g>
    </svg>

    <span class="arrow" style="left:60px;top:56px"></span>
    <div class="t bullet" style="left:96px;top:59px">Sites updated -</div>
    <div class="t bullet" style="left:154px;top:87px">in LESS THAN A MINUTE</div>
    <span class="arrow" style="left:142px;top:150px"></span>
    <div class="t bullet" style="left:180px;top:153px">NO Contracts</div>
    <span class="arrow" style="left:73px;top:219px"></span>
    <div class="t bullet" style="left:110px;top:222px">Money back GUARANTEE</div>
    <div class="t pounds" style="left:84px;top:262px;font-size:28px;transform:rotate(-10deg)">£££</div>
    <span class="arrow" style="left:202px;top:273px"></span>
    <div class="t bullet" style="left:238px;top:276px">From £400 ONLY</div>
    <div class="t pounds" style="left:416px;top:306px;font-size:19px;transform:rotate(-10deg)">£££</div>
    <span class="arrow" style="left:70px;top:332px"></span>
    <div class="t bullet" style="left:107px;top:335px">Promotion via Chatterly,</div>
    <div class="t bullet" style="left:199px;top:367px">Snapvault, Peepline &amp;</div>
    <div class="t bullet" style="left:317px;top:397px">ReelBox etc.</div>

    <div class="offer">
      <span class="offer__big">10% OFF</span>
      <span class="offer__small">with this flyer</span>
      <span class="offer__small">(until 20.12.2010)</span>
    </div>

    <div class="t contact contact--phone" style="left:28px;top:638px">020 7946 0381</div>
    <div class="t contact contact--email" style="left:28px;top:663px">info@brightnetstall.co.uk</div>

    <div class="brand" style="left:292px;top:640px">
      <span class="brand__mark"></span><span class="brand__name">Bright Net Stall</span>
    </div>
  </section>

  <div class="brand" style="left:48px;top:815px">
    <span class="brand__mark"></span><span class="brand__name">Bright Net Stall</span>
  </div>

</div>
</body>
</html>
```